Talent Management Company Needs Business Cards

Using one of the logos provided (attached) K&R Talent Collective needs a business card designed.
Please visit our website for more information about us-

www.krtalentcollective.example

The face should feature a dramatic presentation of the logo with the back being reserved for our professional information which is:

The information should be:
Dorian T. Vickers
C.E.O
Email: dtvickers@krtalentcollective.example
Mobile: 555-804-2917
Website: www.krtalentcollective.example

Marcus L. Vickers
Director of Public Relations
Email: mlvickers@krtalentcollective.example
Mobile: 555-806-3350

Jules R. Hampton
Director of Client Development
Email: jhampton@krtalentcollective.example

Simon Hurlock
Director of Brand Development
Email: shurlock@krtalentcollective.example

Would like the logo to have color. I would like to see one side red or black and the other side white but if it looks better in either black or red that would be fine to but would like to see how it comes out.

Please feel free to message me and if you would like just the icon alone I have other image files that I can send as well.

Target Market(s)

Professional Athletes, coaches, entertainers age 18-35 but also must be accepted in the business community

Industry/Entity Type

Business

Requirements
Must have
• 1) Use the logo
2) Double sided
3) Distinctive
Nice to have
• Small simple images for telephone, e-mail, and Url.

```html
<!DOCTYPE html>
<html lang="en">
<head>
<meta charset="utf-8">
<title>K&amp;R Talent Collective — Business Card</title>
<link rel="stylesheet" href="https://fonts.googleapis.com/css2?family=Didact+Gothic&display=swap">
<style>
  :root {
    --page-bg: #ffffff;
    --card-light: #2e2e2e;
    --card-dark: #0a0a0a;
    --ray-tone: #1c1c1c;
    --brand-red: #c8161d;
    --tag-text: #ecc3c3;
    --shadow: rgba(0, 0, 0, 0.35);
  }
  html, body {
    margin: 0;
    padding: 0;
    width: 1200px;
    height: 1004px;
    overflow: hidden;
    background: var(--page-bg);
  }
  .canvas {
    position: relative;
    width: 1200px;
    height: 1004px;
  }
  .card {
    position: absolute;
    display: block;
    filter: drop-shadow(0 2px 3px var(--shadow));
  }
  .card--large { left: 133px; top: 60px; width: 934px; height: 550px; }
  .card--small { left: 341px; top: 663px; width: 482px; height: 304px; }
  .card__light { fill: var(--card-light); }
  .card__dark { fill: var(--card-dark); }
  .brand-tag {
    font-family: "Didact Gothic", sans-serif;
    font-size: 19px;
    letter-spacing: 2px;
    fill: var(--tag-text);
  }
  .brand-dot { fill: var(--brand-red); }
  .holder-name {
    font-family: "Didact Gothic", sans-serif;
    font-size: 44px;
    fill: var(--brand-red);
  }
</style>
</head>
<body>
<main class="canvas">

  <svg class="card card--large" viewBox="0 0 700 412" aria-label="Business card front">
    <defs>
      <clipPath id="card-shape-lg">
        <path d="M115,0 L660,0 Q700,0 700,40 L700,372 Q700,412 660,412 L0,412 L0,115 Z"/>
      </clipPath>
      <radialGradient id="burst-lg" cx="120" cy="330" r="620" gradientUnits="userSpaceOnUse">
        <stop offset="0" stop-color="#262626"/>
        <stop offset="0.5" stop-color="#141414"/>
        <stop offset="1" stop-color="#0a0a0a"/>
      </radialGradient>
    </defs>
    <g clip-path="url(#card-shape-lg)">
      <rect class="card__light" x="0" y="0" width="700" height="412"/>
      <polygon class="card__dark" points="475,0 700,0 700,412 65,412"/>
      <g role="img" aria-label="Sunburst of dark rays radiating from the lower left">
        <polygon points="475,0 700,0 700,412 65,412" fill="url(#burst-lg)"/>
      </g>
    </g>
    <circle class="brand-dot" cx="118" cy="213" r="26"/>
    <text class="brand-tag" x="0" y="0" textLength="350" lengthAdjust="spacingAndGlyphs"
          transform="translate(54,398) rotate(-45)">K &amp; R TALENT COLLECTIVE</text>
    <text class="holder-name" x="327" y="292">Dorian T. Vickers</text>
  </svg>

  <svg class="card card--small" viewBox="0 0 700 412" aria-label="Business card front, small">
    <defs>
      <clipPath id="card-shape-sm">
        <path d="M115,0 L650,0 Q700,0 700,50 L700,362 Q700,412 650,412 L0,412 L0,115 Z"/>
      </clipPath>
      <radialGradient id="burst-sm" cx="120" cy="330" r="620" gradientUnits="userSpaceOnUse">
        <stop offset="0" stop-color="#262626"/>
        <stop offset="0.5" stop-color="#141414"/>
        <stop offset="1" stop-color="#0a0a0a"/>
      </radialGradient>
    </defs>
    <g clip-path="url(#card-shape-sm)">
      <rect class="card__light" x="0" y="0" width="700" height="412"/>
      <polygon class="card__dark" points="475,0 700,0 700,412 65,412"/>
      <g role="img" aria-label="Sunburst of dark rays radiating from the lower left">
        <polygon points="475,0 700,0 700,412 65,412" fill="url(#burst-sm)"/>
      </g>
    </g>
    <circle class="brand-dot" cx="118" cy="213" r="26"/>
    <text class="brand-tag" x="0" y="0" textLength="350" lengthAdjust="spacingAndGlyphs"
          transform="translate(54,398) rotate(-45)">K &amp; R TALENT COLLECTIVE</text>
    <text class="holder-name" x="327" y="292">Dorian T. Vickers</text>
  </svg>

</main>
</body>
</html>
```